Do it yourself blood pressure poster and flyer

I work in a Drs Health Centre. We have a pod where patients can do their own blood pressure, height, weight etc. We'd like to design a poster and a flyer to encourage patients to use it. The poster would be on display in the waiting room and the flyer would be given to patients. Once in the pod, the measurements are easy to do and take less than 5 minutes.
Our name is Brynhafod Health Centre

Target Market(s)

Patinets in a deprived area, UK

Industry/Entity Type

Health Care

Requirements
Must have
• Eye catching; encourage patients to use self measurement of blood pressure
Nice to have
• Not too serious. Only takes a few minutes. Give result to Receptionist or Dr

```html
<!DOCTYPE html>
<html lang="en">
<head>
<meta charset="utf-8">
<title>Brynhafod Health Centre – Self Check Pod</title>
<link rel="stylesheet" href="https://fonts.googleapis.com/css2?family=Michroma&family=Tenor+Sans&display=swap">
<style>
  :root {
    --ink: #111111;
    --brand-blue: #1a72b8;
    --accent-blue: #2a7fc1;
    --sky-light: #eef7fc;
    --sky-mid: #c6e5f6;
    --sky-deep: #a6d6f1;
    --paper: #ffffff;
    --footer-blue: #0f70b8;
  }
  html, body {
    margin: 0;
    padding: 0;
    overflow: hidden;
    background: var(--paper);
  }
  .poster {
    position: relative;
    width: 848px;
    height: 1200px;
    overflow: hidden;
    background: var(--paper);
    font-family: "Michroma", sans-serif;
    color: var(--ink);
  }
  .hero-band {
    position: absolute;
    left: 0; top: 0;
    width: 848px; height: 566px;
    background: linear-gradient(90deg, var(--paper) 0%, var(--sky-light) 30%, var(--sky-mid) 62%, var(--sky-deep) 100%);
  }
  .doctor-photo {
    position: absolute;
    left: 0; top: 0;
    width: 345px; height: 566px;
    background: radial-gradient(ellipse at 45% 45%, #f4f6f8 0%, #e3ebf0 45%, rgba(230,242,250,0) 80%);
  }
  .headline {
    position: absolute;
    left: 350px; top: 30px;
    width: 410px;
    text-align: center;
    margin: 0;
  }
  .headline-now {
    display: block;
    font-size: 104px;
    line-height: 1;
    letter-spacing: 2px;
    margin-left: -20px;
  }
  .headline-line {
    display: block;
    font-size: 21px;
    letter-spacing: 2px;
    line-height: 1;
  }
  .headline-line.lead { margin-top: 42px; }
  .headline-feature {
    display: block;
    font-size: 33px;
    letter-spacing: 3px;
    color: var(--brand-blue);
    line-height: 1;
  }
  .headline-feature.first { margin-top: 42px; }
  .headline-feature.second { margin-top: 34px; }
  .headline-line.checked { margin-top: 42px; }
  .headline-line.minutes { margin-top: 44px; }
  .device-photo {
    position: absolute;
    left: 374px; top: 526px;
    width: 377px; height: 377px;
    border-radius: 50%;
    border: 4px solid var(--brand-blue);
    box-sizing: border-box;
    background: radial-gradient(circle at 40% 55%, #f3f1ea 0%, #e6e3da 40%, #ffffff 75%);
  }
  .benefits {
    position: absolute;
    left: 20px; top: 716px;
    width: 320px;
    margin: 0;
    text-align: center;
    font-family: "Tenor Sans", sans-serif;
    font-size: 24px;
    line-height: 36px;
    color: var(--ink);
  }
  .tagline {
    position: absolute;
    right: 58px; top: 978px;
    margin: 0;
    font-size: 31px;
    letter-spacing: 2px;
    line-height: 1;
    white-space: nowrap;
  }
  .tagline .divider {
    display: inline-block;
    width: 2px;
    height: 30px;
    background: var(--accent-blue);
    vertical-align: -3px;
    margin: 0 16px;
  }
  .footer-band {
    position: absolute;
    left: 0; top: 1081px;
    width: 848px; height: 119px;
    background: var(--footer-blue);
    color: var(--paper);
    text-align: center;
    font-family: "Tenor Sans", sans-serif;
  }
  .centre-name {
    margin: 26px 0 0;
    font-size: 34px;
    font-weight: normal;
    letter-spacing: -0.5px;
    line-height: 1;
  }
  .centre-address {
    margin: 18px 0 0;
    font-size: 12px;
    letter-spacing: 0.3px;
  }
</style>
</head>
<body>
<main class="poster">
  <div class="hero-band"></div>
  <div class="doctor-photo" role="img" aria-label="Smiling doctor in a white coat with a stethoscope, holding a clipboard"></div>

  <h1 class="headline">
    <span class="headline-now">Now</span>
    <span class="headline-line lead">you can do your own</span>
    <span class="headline-feature first">blood pressure,</span>
    <span class="headline-feature second">height, weight</span>
    <span class="headline-line checked">checked in less than</span>
    <span class="headline-line minutes">5 mins</span>
  </h1>

  <div class="device-photo" role="img" aria-label="Patient placing her arm into an automatic blood pressure monitor"></div>

  <p class="benefits">Not too serious.<br>Only takes a few minutes<br>Gives result to<br>Receptionist or Doctor</p>

  <p class="tagline">QUICK<span class="divider"></span>EASY<span class="divider"></span>SAFE</p>

  <footer class="footer-band">
    <h2 class="centre-name">Brynhafod Health Centre</h2>
    <p class="centre-address">Heol Glas, Brynhafod, Cardiff, CF9 4QR</p>
  </footer>
</main>
</body>
</html>
```